Packaging & Label Design for CDB Products

We are a European CBD company specialising in athletic recovery, sleep improvement and wellness.

We would like the packaging to incorporate our logo and name (and font 'Codec') 'Meridell CBD'. The design must be transferable to all of our products. CBD Oils, Balms, Lip Balm and Vape E-Liquid.

We would like it to be simple but eye-catching and modern. We don't want bright colours. Preferred pallet of muted greys, blacks, white and pastel colours. Geometric concepts, possibly using different colours for each item of the range, we are open to new and fresh ideas (we are seeking you for your experience) and when we find the right design we would likely throw more work in your direction..

Our product range is not complete so the designer must be flexible with some changes and provide files where format can be easily edited by packaging manufacturer. We are also waiting for dimensions for the labels and boxes for several products and will supply the designer with full dimensions of all products once selected.

Oil Box: 2.6 x 9.0 x 2.6 cm (open format 16.7 x 11.6cm)
Labels: 7.8 x 3.3 cm (Front and Back)

Our expected product range will be:
CBD Oil 1000mg
CBD Oil 3000mg
CBD Balm 100mg
CBD Balm 300mg
E-Liquid 500mg
Lip Balm 50mg

We look forward to seeing your ideas.

Best Regards
Meridell CBD

```html
<!DOCTYPE html>
<html lang="en">
<head>
<meta charset="utf-8">
<title>Meridell CBD — Label Range</title>
<link rel="stylesheet" href="https://fonts.googleapis.com/css2?family=Montserrat:wght@500;600&family=Open+Sans:wght@400&display=swap">
<style>
  :root {
    --canvas: #ffffff;
    --ink-light: #ffffff;
    --ink-dark: #231f20;
    --oil-bg: #56625f;
    --oil-strong-tri: #958ca6;
    --oil-strong-shade: #b7cdb9;
    --oil-mild-tri: #9a8088;
    --oil-mild-shade: #b9c8b5;
    --balm-bg: #1b4d47;
    --balm-mild-tri: #4f8a80;
    --balm-mild-shade: #8aa39b;
    --balm-strong-tri: #d8dd8e;
    --balm-strong-shade: #6b8a7e;
    --liquid-bg: #231f20;
    --liquid-tri: #26304a;
    --liquid-shade: #7a8a60;
    --lip-bg: #ffffff;
    --lip-tri: #f3d9cf;
    --lip-shade: #d5e8cc;
    --lip-border: #c9c9c9;
  }
  html, body {
    margin: 0;
    padding: 0;
    width: 1200px;
    height: 1200px;
    overflow: hidden;
    background: var(--canvas);
  }
  .range {
    position: relative;
    width: 1200px;
    height: 1200px;
  }
  .label {
    position: absolute;
    width: 234px;
    height: 552px;
    overflow: hidden;
    background: var(--bg);
    color: var(--ink, var(--ink-light));
    box-sizing: border-box;
  }
  .label--oil-3000   { left: 98px;  top: 34px;  --bg: var(--oil-bg);    --tri: var(--oil-strong-tri);  --shade: var(--oil-strong-shade); }
  .label--balm-100   { left: 480px; top: 34px;  --bg: var(--balm-bg);   --tri: var(--balm-mild-tri);   --shade: var(--balm-mild-shade); }
  .label--balm-300   { left: 860px; top: 34px;  --bg: var(--balm-bg);   --tri: var(--balm-strong-tri); --shade: var(--balm-strong-shade); }
  .label--oil-1000   { left: 98px;  top: 618px; --bg: var(--oil-bg);    --tri: var(--oil-mild-tri);    --shade: var(--oil-mild-shade); }
  .label--liquid-500 { left: 480px; top: 618px; --bg: var(--liquid-bg); --tri: var(--liquid-tri);      --shade: var(--liquid-shade); }
  .label--lip-50     { left: 860px; top: 618px; --bg: var(--lip-bg);    --tri: var(--lip-tri);         --shade: var(--lip-shade);
                       --ink: var(--ink-dark); border: 1px solid var(--lip-border); }

  .brand {
    position: absolute;
    top: 36px;
    left: 0;
    right: 0;
    text-align: center;
  }
  .brand-mark {
    display: block;
    width: 58px;
    height: 58px;
    margin: 0 auto 24px;
    border-radius: 50%;
    border: 3px solid currentColor;
    box-sizing: border-box;
  }
  .brand-name {
    font-family: "Montserrat", sans-serif;
    font-weight: 600;
    font-size: 23px;
    letter-spacing: 1.5px;
    white-space: nowrap;
  }
  .product {
    position: absolute;
    top: 290px;
    left: 0;
    right: 0;
    text-align: center;
  }
  .product-name {
    margin: 0;
    font-family: "Montserrat", sans-serif;
    font-weight: 500;
    font-size: 26px;
    letter-spacing: 0.5px;
  }
  .product-strength {
    margin: 18px 0 0;
    font-family: "Open Sans", sans-serif;
    font-weight: 400;
    font-size: 17px;
  }
  .pattern {
    position: absolute;
    left: 0;
    right: 0;
    top: 302px;
    bottom: 0;
    background: linear-gradient(135deg, var(--tri) 0%, var(--tri) 55%, var(--shade) 100%);
    clip-path: polygon(100% 0, 100% 100%, 0 100%, 0 75%, 25% 75%, 25% 50%, 50% 50%, 50% 25%, 75% 25%, 75% 0);
  }
  .product { z-index: 1; }
</style>
</head>
<body>
<main class="range">

  <section class="label label--oil-3000">
    <div class="brand"><span class="brand-mark"></span><span class="brand-name">MERIDELL CBD</span></div>
    <div class="pattern" role="img" aria-label="Geometric triangle pattern in lilac and pale sage"></div>
    <div class="product"><h2 class="product-name">CBD OIL</h2><p class="product-strength">3000mg</p></div>
  </section>

  <section class="label label--balm-100">
    <div class="brand"><span class="brand-mark"></span><span class="brand-name">MERIDELL CBD</span></div>
    <div class="pattern" role="img" aria-label="Geometric triangle pattern in sea green and grey"></div>
    <div class="product"><h2 class="product-name">CBD BALM</h2><p class="product-strength">100mg</p></div>
  </section>

  <section class="label label--balm-300">
    <div class="brand"><span class="brand-mark"></span><span class="brand-name">MERIDELL CBD</span></div>
    <div class="pattern" role="img" aria-label="Geometric triangle pattern in pale lime and grey green"></div>
    <div class="product"><h2 class="product-name">CBD BALM</h2><p class="product-strength">300mg</p></div>
  </section>

  <section class="label label--oil-1000">
    <div class="brand"><span class="brand-mark"></span><span class="brand-name">MERIDELL CBD</span></div>
    <div class="pattern" role="img" aria-label="Geometric triangle pattern in dusty mauve and pale sage"></div>
    <div class="product"><h2 class="product-name">CBD OIL</h2><p class="product-strength">1000mg</p></div>
  </section>

  <section class="label label--liquid-500">
    <div class="brand"><span class="brand-mark"></span><span class="brand-name">MERIDELL CBD</span></div>
    <div class="pattern" role="img" aria-label="Geometric triangle pattern in navy and olive"></div>
    <div class="product"><h2 class="product-name">E-LIQUID</h2><p class="product-strength">500mg</p></div>
  </section>

  <section class="label label--lip-50">
    <div class="brand"><span class="brand-mark"></span><span class="brand-name">MERIDELL CBD</span></div>
    <div class="pattern" role="img" aria-label="Geometric triangle pattern in blush pink and mint"></div>
    <div class="product"><h2 class="product-name">LIP BALM</h2><p class="product-strength">50mg</p></div>
  </section>

</main>
</body>
</html>
```